Sheriff Candidate needs a large yard sign

A candidate for Sheriff needs to have a sign to put in front of businesses and houses that advertise her candidacy.

Target Market(s)

Democrats, voters

Industry/Entity Type

Political

Font styles to use
Sans Serif

Colors
34a7d7
3276b5

Requirements
Must have
• Must have her picture
• Must have the words "Elect Dana Whitlock" - I'd like the name Dana to be smaller Whitlock. "Elect" and "Whitlock" should be the focus.
• at the bottom in a box "Paid for by the Committee to Elect Dana Whitlock"
Nice to have
• it would be good to have her logo as well.
• blue color for democrats and on a white background
Should not have
• pink color

```html
<!DOCTYPE html>
<html lang="en">
<head>
<meta charset="utf-8">
<title>Elect Dana Whitlock – Yard Sign</title>
<link href="https://fonts.googleapis.com/css2?family=Patua+One&display=swap" rel="stylesheet">
<style>
  :root {
    --blue-deep: #3276b5;
    --blue-sky: #34a7d7;
    --white: #ffffff;
    --ink-blue: #3a72b0;
    --photo-dark: #1f2a3d;
    --photo-light: #c9a896;
  }
  html, body {
    margin: 0;
    padding: 0;
    width: 1200px;
    height: 848px;
    overflow: hidden;
    background: var(--white);
  }
  .sign {
    position: relative;
    width: 1200px;
    height: 848px;
    overflow: hidden;
    background: var(--white);
    font-family: "Patua One", sans-serif;
  }
  .bands {
    position: absolute;
    inset: 0;
  }
  .headline-elect {
    font-family: "Patua One", sans-serif;
    font-size: 238px;
    fill: var(--white);
  }
  .campaign-mark {
    position: absolute;
    left: 40px;
    top: 60px;
    display: flex;
    align-items: center;
    gap: 14px;
  }
  .campaign-mark__dot {
    width: 52px;
    height: 52px;
    border-radius: 50%;
    background: var(--blue-deep);
  }
  .campaign-mark__name {
    color: var(--blue-deep);
    font-size: 28px;
    line-height: 1;
  }
  .candidate-name {
    position: absolute;
    right: 466px;
    top: 428px;
    margin: 0;
    text-align: right;
    color: var(--white);
    line-height: 1;
  }
  .candidate-name__first {
    display: block;
    font-size: 76px;
  }
  .candidate-name__last {
    display: block;
    font-size: 100px;
  }
  .disclaimer {
    position: absolute;
    left: 56px;
    top: 640px;
    margin: 0;
    color: var(--ink-blue);
    line-height: 1;
  }
  .disclaimer__line {
    display: block;
    font-size: 60px;
  }
  .disclaimer__line--final {
    font-size: 56px;
  }
  .disclaimer__big {
    font-size: 80px;
  }
  .candidate-photo {
    position: absolute;
    left: 762px;
    top: 20px;
    width: 438px;
    height: 828px;
    border-radius: 200px 200px 0 0;
    background: linear-gradient(180deg, var(--photo-light) 0%, var(--photo-light) 30%, var(--photo-dark) 45%, var(--photo-dark) 100%);
  }
</style>
</head>
<body>
  <main class="sign">
    <svg class="bands" width="1200" height="848" viewBox="0 0 1200 848" role="img" aria-label="Elect">
      <rect class="band-sky" x="0" y="385" width="1200" height="242" fill="var(--blue-sky)"/>
      <polygon class="band-deep" points="0,335 912,0 1200,0 1200,200 0,590" fill="var(--blue-deep)"/>
      <line class="band-rule" x1="72" y1="548" x2="665" y2="330" stroke="var(--white)" stroke-width="5"/>
      <text class="headline-elect" x="88" y="516" transform="rotate(-20.2 88 516)">Elect</text>
    </svg>

    <div class="campaign-mark">
      <span class="campaign-mark__dot"></span>
      <span class="campaign-mark__name">Whitlock for Sheriff</span>
    </div>

    <p class="candidate-name">
      <span class="candidate-name__first">Dana</span>
      <span class="candidate-name__last">Whitlock</span>
    </p>

    <p class="disclaimer">
      <span class="disclaimer__line">Paid for by the</span>
      <span class="disclaimer__line">Committee to</span>
      <span class="disclaimer__line disclaimer__line--final"><span class="disclaimer__big">Elect</span> Dana <span class="disclaimer__big">Whitlock</span></span>
    </p>

    <div class="candidate-photo" role="img" aria-label="Portrait photo of candidate Dana Whitlock, smiling, in a dark blazer"></div>
  </main>
</body>
</html>
```